Business Card Design

Bramwell Pantry is the name of my health coaching business. My tag line is "Where good health meets real life." I will be working with clients one-on-one and in groups. My target clients are women "of a certain age" who want to be more comfortable in their own skin. We will work together in a 6-month program. The coaching sessions will take place in my kitchen. I will also be conducting monthly cooking classes and field trips - to farmer's markets, speciality markets etc.. for my clients.
Updates

the business name is Bramwell Pantry - I'm not sure how the p got in there at the end of the name

Thank you

Please include the website - www.bramwellpantry-example.com and the tag line:

Where good health meets real life on the business card.

Thank you

Please add the phone number to the business card - sorry, I forgot to state that in the original brief

(555) 218-4476

Target Market(s)

Women "of a certain age" who want to be more comfortable in their own skin

Industry/Entity Type

Cooking

Contact Information for Business Card

Bramwell Pantry
Where good health meets real life

Harriet Dunmore
Health Coach
(555) 218-4476

Font styles to use
Serif
Sans Serif

Requirements
Must have
• front & back design
I typical like soft colors - and have tended toward greens over time - I'm open although I would not like bright reds, yellows etc..

```html
<!DOCTYPE html>
<html lang="en">
<head>
<meta charset="utf-8">
<title>Bramwell Pantry – Business Card</title>
<link rel="stylesheet" href="https://fonts.googleapis.com/css2?family=Arimo:wght@400&family=PT+Sans:wght@400&display=swap">
<style>
  :root {
    --paper: #ffffff;
    --olive: #5f5e4c;
    --sky: #4fd0ee;
    --brand-blue: #2f7fe8;
    --ink: #111111;
    --white: #ffffff;
  }
  html, body {
    margin: 0;
    padding: 0;
    width: 1200px;
    height: 747px;
    overflow: hidden;
    background: var(--paper);
  }
  .canvas {
    position: relative;
    width: 1200px;
    height: 747px;
    background: var(--paper);
    font-family: "Arimo", Arial, sans-serif;
  }
  .card {
    position: absolute;
    left: 30px;
    top: 28px;
    width: 1147px;
    height: 693px;
    box-sizing: border-box;
    border: 3px solid var(--ink);
    border-right: none;
    border-radius: 51px 0 0 32px;
    background: var(--paper);
  }
  .contact-panel {
    position: absolute;
    left: 470px;
    top: 27px;
    width: 707px;
    height: 696px;
    background: var(--olive);
  }
  .brand-mark {
    position: absolute;
    left: 128px;
    top: 268px;
    display: flex;
    align-items: center;
    gap: 10px;
    color: var(--brand-blue);
    font-size: 22px;
    line-height: 1;
  }
  .brand-mark .square {
    width: 16px;
    height: 16px;
    background: var(--brand-blue);
  }
  .business-name {
    position: absolute;
    right: 742px;
    top: 382px;
    margin: 0;
    color: var(--olive);
    font-weight: 400;
    font-size: 66px;
    line-height: 90px;
    text-align: right;
    letter-spacing: 0;
    white-space: nowrap;
  }
  .person {
    position: absolute;
    left: 470px;
    width: 707px;
    top: 240px;
    text-align: center;
  }
  .person-name {
    margin: 0 0 0 72px;
    color: var(--sky);
    font-weight: 400;
    font-size: 65px;
    line-height: 74px;
  }
  .person-role {
    margin: -8px 0 0 0;
    color: var(--white);
    font-size: 52px;
    line-height: 60px;
    padding-left: 0;
  }
  .contact-list {
    position: absolute;
    left: 517px;
    top: 432px;
    margin: 0;
    padding: 0;
    list-style: none;
    color: var(--sky);
  }
  .contact-list li { white-space: nowrap; }
  .contact-phone {
    font-family: "PT Sans", Arial, sans-serif;
    font-size: 31px;
    line-height: 38px;
  }
  .contact-email {
    font-size: 29px;
    line-height: 44px;
    letter-spacing: -0.6px;
  }
  .contact-web {
    font-size: 32px;
    line-height: 48px;
    letter-spacing: 0.4px;
  }
  .tagline {
    position: absolute;
    left: 129px;
    top: 612px;
    margin: 0;
    font-size: 58px;
    line-height: 70px;
    white-space: nowrap;
    color: var(--olive);
  }
  .tagline-over-panel {
    position: absolute;
    left: 470px;
    top: 612px;
    width: 707px;
    height: 80px;
    overflow: hidden;
  }
  .tagline-over-panel .tagline {
    left: -341px;
    top: 0;
    color: var(--white);
  }
</style>
</head>
<body>
<main class="canvas">
  <section class="card" aria-label="Business card"></section>
  <div class="contact-panel"></div>

  <div class="brand-mark"><span class="square"></span><span>Bramwell Pantry</span></div>

  <h1 class="business-name">BRAMWELL<br>PANTRY</h1>

  <div class="person">
    <h2 class="person-name">Harriet Dunmore</h2>
    <p class="person-role">Health Coach</p>
  </div>

  <ul class="contact-list">
    <li class="contact-phone">Phone : (555) 218-4476</li>
    <li class="contact-email">harriet@bramwellpantry-example.com</li>
    <li class="contact-web">www.bramwellpantry-example.com</li>
  </ul>

  <p class="tagline">“Where good health meets real life”</p>
  <div class="tagline-over-panel" aria-hidden="true">
    <p class="tagline">“Where good health meets real life”</p>
  </div>
</main>
</body>
</html>
```